Personal training poster - 1200X900mm

Poster to promote my new personal training service at my gym. The poster will be printed and put into an aframe to be seen by people walking past my gym. It needs to be simple and eye catching with the text i have put in the must haves. The text and image should be the prominent parts of the design.

Target Market(s)

30-50 year old females

Industry/Entity Type

Fitness

Font styles to use
Sans Serif

Requirements
Must have
• my logo
• exercise graphic
• Must include the following text:
• Are you looking for a personal trainer? Our expert trainers can help you achieve you take your health and fitness back!
• Contact details:
• 1300452968
• info@brightmovegym.com.au
• Located under the Harbourview Club

```html
<!DOCTYPE html>
<html lang="en">
<head>
<meta charset="utf-8">
<title>Personal Trainer Posters – Brightmove Gym</title>
<link rel="stylesheet" href="https://fonts.googleapis.com/css2?family=Bebas+Neue&family=Montserrat:wght@600&display=swap">
<style>
  :root {
    --ink: #0b0b0b;
    --paper: #ffffff;
    --sun: #fdd00f;
    --sun-soft: #fcdb85;
    --sky: #2f73b8;
    --navy: #1d3f78;
  }
  html, body {
    margin: 0;
    padding: 0;
    width: 1200px;
    height: 778px;
    overflow: hidden;
    background: var(--paper);
  }
  .sheet {
    position: relative;
    width: 1200px;
    height: 778px;
  }
  .poster {
    position: absolute;
    top: 11px;
    width: 537px;
    height: 713px;
    transform: scale(1.0616);
    transform-origin: 0 0;
    overflow: hidden;
    background: var(--paper);
  }
  .poster--woman { left: 11px; }
  .poster--man { left: 620px; }

  .poster__shapes {
    position: absolute;
    inset: 0;
    width: 537px;
    height: 713px;
  }

  .brand {
    position: absolute;
    left: 32px;
    top: 34px;
    display: flex;
    align-items: center;
    gap: 8px;
    font-family: "Bebas Neue", "Oswald", sans-serif;
    font-size: 26px;
    line-height: 1;
    color: var(--navy);
  }
  .brand__dot {
    width: 30px;
    height: 30px;
    border-radius: 50%;
    background: var(--navy);
  }

  .headline {
    position: absolute;
    left: 38px;
    top: 184px;
    margin: 0;
    font-family: "Bebas Neue", "Oswald", sans-serif;
    font-weight: 400;
    color: var(--sun);
    line-height: 1;
  }
  .headline__lead {
    display: block;
    font-size: 52px;
    line-height: 48px;
  }
  .headline__main {
    display: block;
    font-size: 92px;
    line-height: 78px;
    margin-top: 6px;
  }

  .pitch {
    position: absolute;
    left: 38px;
    top: 444px;
    width: 285px;
    margin: 0;
    font-family: "Montserrat", sans-serif;
    font-weight: 600;
    font-size: 16.5px;
    line-height: 24.5px;
    color: var(--paper);
  }

  .divider {
    position: absolute;
    left: 38px;
    top: 537px;
    width: 47px;
    height: 5px;
    background: var(--sun);
  }

  .contact {
    position: absolute;
    left: 38px;
    top: 578px;
    font-family: "Montserrat", sans-serif;
    font-weight: 600;
    color: var(--paper);
  }
  .contact__phone {
    display: block;
    font-size: 39px;
    line-height: 44px;
    color: var(--sun);
  }
  .contact__email {
    display: block;
    font-size: 16px;
    line-height: 26px;
  }
  .contact__place {
    display: flex;
    align-items: center;
    gap: 5px;
    margin-top: 9px;
    font-size: 12.5px;
  }
  .contact__pin {
    width: 10px;
    height: 14px;
  }
</style>
</head>
<body>
<main class="sheet">

  <article class="poster poster--woman">
    <svg class="poster__shapes" viewBox="0 0 537 713">
      <defs>
        <linearGradient id="photo-woman" x1="0" y1="0" x2="0.3" y2="1">
          <stop offset="0" stop-color="#e7d4c6"/>
          <stop offset="0.3" stop-color="#c58a68"/>
          <stop offset="0.5" stop-color="#a5715a"/>
          <stop offset="0.75" stop-color="#6f6c70"/>
          <stop offset="1" stop-color="#4c4c52"/>
        </linearGradient>
      </defs>
      <rect class="photo" x="90" y="30" width="447" height="683" rx="0" fill="url(#photo-woman)" role="img" aria-label="Photo of a fit woman in sportswear lifting two dumbbells"/>
      <polygon class="band band--blue" points="537,485 537,713 385,713" fill="var(--sky)"/>
      <polygon class="band band--black" points="0,70 0,713 428,713" fill="var(--ink)"/>
      <polygon class="band band--yellow" points="0,0 228,0 0,160" fill="var(--sun-soft)"/>
    </svg>

    <div class="brand"><span class="brand__dot"></span>Brightmove Gym</div>

    <h1 class="headline">
      <span class="headline__lead">Are you<br>looking for a</span>
      <span class="headline__main">Personal<br>Trainer?</span>
    </h1>

    <p class="pitch">Our expert trainers can help you achieve you take your health and fitness back!</p>

    <div class="divider"></div>

    <div class="contact">
      <span class="contact__phone">1300 452 968</span>
      <span class="contact__email">info@brightmovegym.com.au</span>
      <span class="contact__place">
        <svg class="contact__pin" viewBox="0 0 10 14"><path d="M5 0a5 5 0 0 0-5 5c0 3.5 5 9 5 9s5-5.5 5-9a5 5 0 0 0-5-5zm0 7a2 2 0 1 1 0-4 2 2 0 0 1 0 4z" fill="var(--sun)"/></svg>
        Located under the Harbourview Club
      </span>
    </div>
  </article>

  <article class="poster poster--man">
    <svg class="poster__shapes" viewBox="0 0 537 713">
      <defs>
        <linearGradient id="photo-man" x1="0" y1="0" x2="0.4" y2="1">
          <stop offset="0" stop-color="#e3c8b4"/>
          <stop offset="0.3" stop-color="#b57652"/>
          <stop offset="0.55" stop-color="#8e5a3d"/>
          <stop offset="0.8" stop-color="#a8785c"/>
          <stop offset="1" stop-color="#e7dcd4"/>
        </linearGradient>
      </defs>
      <rect class="photo" x="130" y="55" width="407" height="620" fill="url(#photo-man)" role="img" aria-label="Photo of a muscular man leaning forward doing a one-arm dumbbell row"/>
      <polygon class="band band--blue" points="537,485 537,713 385,713" fill="var(--sky)"/>
      <polygon class="band band--black" points="0,80 0,713 428,713" fill="var(--ink)"/>
      <polygon class="band band--yellow" points="0,0 228,0 0,160" fill="var(--sun-soft)"/>
    </svg>

    <div class="brand"><span class="brand__dot"></span>Brightmove Gym</div>

    <h2 class="headline">
      <span class="headline__lead">Are you<br>looking for a</span>
      <span class="headline__main">Personal<br>Trainer?</span>
    </h2>

    <p class="pitch">Our expert trainers can help you achieve you take your health and fitness back!</p>

    <div class="divider"></div>

    <div class="contact">
      <span class="contact__phone">1300 452 968</span>
      <span class="contact__email">info@brightmovegym.com.au</span>
      <span class="contact__place">
        <svg class="contact__pin" viewBox="0 0 10 14"><path d="M5 0a5 5 0 0 0-5 5c0 3.5 5 9 5 9s5-5.5 5-9a5 5 0 0 0-5-5zm0 7a2 2 0 1 1 0-4 2 2 0 0 1 0 4z" fill="var(--sun)"/></svg>
        Located under the Harbourview Club
      </span>
    </div>
  </article>

</main>
</body>
</html>
```